Business Card Design for Small Electrical Contractor

I need to update my business card into something a little more modern. We are a small electrical contracting company. We service domestic and commercial places around Sydney. We have 2 logo designs at the moment. I have uploaded both and 2 different sizes to work with.

Industry/Entity Type

Business

Contact Information for Business Card

Leo Hartigan
8/21-23 Birch Rd, Kelsworth 2087
t - (02) 9381 4720
m - 0427 815 903
E - info@hartiganelx.com.au
W - hartiganelx.com.au
ABN: 42 907 551 316

Font styles to use
Sans Serif

Requirements
Must have
• I would also like to see the below fit on somewhere aswell
• - Licensed Electrician
• - Level 2 (Cat 1 & 4)
• - Domestic
• - Commercial
• - Repairs and Installations
• - Data
Nice to have
• Try and keep similar colours as logo
Should not have
• No lightning bolts or light globes. Smart and professional please.

```html
<!DOCTYPE html>
<html lang="en">
<head>
<meta charset="utf-8">
<title>Hartigan Electrical – Business Card</title>
<link href="https://fonts.googleapis.com/css2?family=Arimo:wght@400;700&family=Montserrat:wght@800&display=swap" rel="stylesheet">
<style>
  :root {
    --bg: #2b2b2b;
    --card-white: #f4f4f4;
    --card-black: #0b0b0b;
    --orange: #e8992b;
    --ink: #5a5a5a;
    --ink-soft: #7a7a7a;
    --paper: #ffffff;
  }
  * { box-sizing: border-box; margin: 0; padding: 0; }
  html, body { width: 1200px; height: 997px; overflow: hidden; }
  body {
    background: var(--bg);
    font-family: "Arimo", Arial, sans-serif;
    position: relative;
  }
  .card {
    position: absolute;
    width: 600px;
    height: 343px;
    border-radius: 18px;
    box-shadow: 0 20px 40px rgba(0,0,0,.45);
  }
  /* Front */
  .card-front { left: 90px; top: 90px; background: var(--card-white); color: var(--ink); }
  .front-brand {
    position: absolute; right: 36px; top: 34px;
    font-size: 20px; font-weight: 400; color: var(--ink);
  }
  .front-credentials {
    position: absolute; right: 36px; top: 110px; text-align: right;
    font-size: 10px; color: var(--ink-soft); line-height: 1.4;
  }
  .front-rule {
    position: absolute; left: 36px; right: 36px; top: 150px; height: 1px;
    background: linear-gradient(to right, var(--ink) 0 55%, var(--orange) 55% 100%);
  }
  .front-web {
    position: absolute; right: 36px; top: 162px;
    font-size: 12px; color: var(--orange);
  }
  .person { position: absolute; left: 36px; top: 190px; }
  .person-name { font-size: 20px; color: var(--ink); }
  .person-title { font-size: 12px; color: var(--orange); margin-top: 2px; }
  .contact-list { position: absolute; left: 36px; top: 248px; list-style: none; }
  .contact-list li {
    display: flex; align-items: center; gap: 10px;
    font-size: 13px; color: var(--ink); height: 19px;
  }
  .contact-icon { width: 13px; height: 13px; flex: none; }
  /* Back */
  .card-back { left: 510px; top: 520px; background: var(--card-black); color: var(--paper); }
  .back-brand {
    position: absolute; left: 0; right: 0; top: 100px; text-align: center;
    font-size: 34px; font-weight: 400; color: var(--paper);
  }
  .services {
    position: absolute; left: 0; right: 0; top: 215px; text-align: center;
    font-family: "Montserrat", Arial, sans-serif; font-weight: 800;
    color: var(--orange); font-size: 16px; letter-spacing: 2px; line-height: 1.8;
  }
  .services .dot { color: var(--paper); margin: 0 8px; }
</style>
</head>
<body>
  <section class="card card-front">
    <div class="front-brand">Hartigan Electrical</div>
    <div class="front-credentials">
      <div>ABN: 42 907 551 316</div>
      <div>Level 2 (Cat 1 &amp; 4)</div>
    </div>
    <div class="front-rule"></div>
    <div class="front-web">www.hartiganelx.com.au</div>
    <div class="person">
      <div class="person-name">Leo Hartigan</div>
      <div class="person-title">Licensed Electrician</div>
    </div>
    <ul class="contact-list">
      <li><svg class="contact-icon" viewBox="0 0 14 14"><circle cx="7" cy="7" r="7" fill="var(--orange)"/><rect x="4" y="5" width="6" height="4" rx="1" fill="#fff"/></svg>(02) 9381 4720</li>
      <li><svg class="contact-icon" viewBox="0 0 14 14"><circle cx="7" cy="7" r="7" fill="var(--orange)"/><rect x="5" y="3.5" width="4" height="7" rx="1" fill="#fff"/></svg>0427 815 903</li>
      <li><svg class="contact-icon" viewBox="0 0 14 14"><circle cx="7" cy="7" r="7" fill="var(--orange)"/><rect x="3.5" y="4.5" width="7" height="5" fill="#fff"/><path d="M3.5 4.5 7 7.5 10.5 4.5" stroke="var(--orange)" fill="none" stroke-width="1"/></svg>info@hartiganelx.com.au</li>
      <li><svg class="contact-icon" viewBox="0 0 14 14"><circle cx="7" cy="7" r="7" fill="var(--orange)"/><path d="M7 3a2.5 2.5 0 0 1 2.5 2.5C9.5 7.5 7 10.5 7 10.5S4.5 7.5 4.5 5.5A2.5 2.5 0 0 1 7 3z" fill="#fff"/></svg>8/21-23 Birch Rd, Kelsworth 2087</li>
    </ul>
  </section>

  <section class="card card-back">
    <div class="back-brand">Hartigan Electrical</div>
    <div class="services">
      <div>DOMESTIC<span class="dot">•</span>COMMERCIAL<span class="dot">•</span>DATA</div>
      <div>REPAIRS &amp; INSTALLATIONS</div>
    </div>
  </section>
</body>
</html>
```